Oil and gas industry project solutions company needs professional cards with Canadian aboriginal fee

We are a aboriginally owned company that is focused on Project Planning, Management, Inspection & Consulting for Canada's Petroleum Industry. We have a logo that we would like to incorporate into a professional looking business card. We are professionals that offer services from project inception to completion.

Target Market(s)

Major industry leaders like NorthRidge Pipelines, Vantor, Kelstrand Energy, Brimwell etc.

Industry/Entity Type

Industry

Contact Information for Business Card

Reid Forbin
reid@kolbymarsh.ca
555 418 9067

Requirements
Must have
• KolbyMarsh Inc. logo.
• Address is: RR4, Site2, Comp7 Pine Hollow, ZZ A0A 8K3 Traditional Territory of the Treaty 8 People
• Colors that are in logo
• Banner or picture on back
• Ability to put different names and contacts
• Website: kolbymarsh.ca
• "Project Planning, Management, Inspection & Consulting for Canada's Petroleum Industry"

```html
<!DOCTYPE html>
<html lang="en">
<head>
<meta charset="utf-8">
<title>KolbyMarsh Inc. Business Card</title>
<link rel="stylesheet" href="https://fonts.googleapis.com/css2?family=Montserrat:wght@400;500;800&display=swap">
<style>
  :root {
    --navy: #232a6b;
    --green: #6cb043;
    --grey: #5a5a5a;
    --white: #ffffff;
    --page: #e9e6e1;
    --photo-site: linear-gradient(135deg, #7a8fa8 0%, #c9b24a 45%, #6b5a3e 100%);
    --photo-snow: linear-gradient(160deg, #9fb3c8 0%, #e4ecf3 50%, #4a5563 100%);
    --photo-pipe: linear-gradient(120deg, #8a6a3e 0%, #d8c24a 50%, #5b4a36 100%);
  }
  * { box-sizing: border-box; margin: 0; padding: 0; }
  html, body { width: 1200px; height: 900px; overflow: hidden; }
  body {
    background: var(--page);
    font-family: "Montserrat", sans-serif;
    position: relative;
  }
  .card {
    position: absolute;
    left: 250px;
    width: 700px;
    height: 400px;
    background: var(--white);
    overflow: hidden;
    box-shadow: 0 6px 18px rgba(0,0,0,0.18);
  }
  .card-back { top: 30px; }
  .card-front { top: 470px; }

  .photo { position: absolute; }
  .photo-site { background: var(--photo-site); }
  .photo-snow { background: var(--photo-snow); }
  .photo-pipe { background: var(--photo-pipe); }

  .brand {
    position: absolute;
    display: flex;
    align-items: center;
    gap: 16px;
  }
  .brand-dot {
    width: 46px; height: 46px;
    border-radius: 50%;
    background: var(--green);
  }
  .brand-name {
    font-weight: 800;
    font-size: 44px;
    color: var(--navy);
    letter-spacing: -1px;
    white-space: nowrap;
  }
  .brand-rule {
    position: absolute;
    height: 1.5px;
    background: var(--grey);
  }

  /* back */
  .card-back .band-white {
    position: absolute; left: 0; top: 100px; width: 700px; height: 130px;
    background: linear-gradient(180deg, #fff 70%, #e6e6e6 100%);
  }
  .card-back .brand { left: 150px; top: 140px; }

  /* front */
  .front-art { position: absolute; inset: 0; }
  .card-front .brand { left: 60px; top: 80px; }
  .name {
    position: absolute; left: 490px; top: 186px;
    color: var(--white); font-size: 28px; font-weight: 500;
  }
  .contacts {
    position: absolute; left: 40px; top: 260px;
    list-style: none; color: var(--white);
  }
  .contacts li {
    display: flex; align-items: center; gap: 12px;
    font-size: 15px; font-weight: 500; line-height: 23px;
  }
  .contacts li:first-child { font-size: 19px; }
  .contacts svg { width: 16px; height: 16px; flex: none; }
</style>
</head>
<body>

<section class="card card-back">
  <div class="photo photo-site" style="left:0;top:0;width:700px;height:100px" role="img" aria-label="Photo of yellow pipelayer machines on a pipeline construction site"></div>
  <div class="band-white"></div>
  <div class="brand">
    <span class="brand-dot"></span>
    <span class="brand-name">KolbyMarsh Inc.</span>
  </div>
  <div class="brand-rule" style="left:222px;top:205px;width:380px"></div>
  <div class="photo photo-pipe" style="left:0;top:230px;width:350px;height:170px" role="img" aria-label="Photo of a yellow-coated pipeline with equipment in the field"></div>
  <div class="photo photo-snow" style="left:354px;top:230px;width:346px;height:170px" role="img" aria-label="Photo of workers in safety vests lowering pipe in a snowy trench"></div>
</section>

<section class="card card-front">
  <svg class="front-art" viewBox="0 0 700 400" width="700" height="400" aria-hidden="true">
    <line x1="0" y1="238" x2="560" y2="238" stroke="var(--navy)" stroke-width="2"/>
    <path d="M0 242 H520 Q560 242 560 290 V360 H0 Z" fill="var(--green)"/>
    <path d="M560 230 H700 V400 H0 V368 H560 Z" fill="#9fb3c8"/>
    <rect x="440" y="176" width="260" height="50" fill="var(--navy)"/>
    <line x1="440" y1="230" x2="700" y2="230" stroke="var(--navy)" stroke-width="2"/>
    <circle cx="440" cy="200" r="38" fill="var(--white)"/>
    <circle cx="440" cy="200" r="32" fill="var(--navy)"/>
    <circle cx="440" cy="190" r="9" fill="var(--white)"/>
    <path d="M424 218 Q440 200 456 218 Z" fill="var(--white)"/>
  </svg>
  <div class="photo photo-snow" style="left:562px;top:232px;width:138px;height:136px" role="img" aria-label="Photo of pipeline crew working in snow"></div>
  <div class="photo photo-site" style="left:0;top:370px;width:700px;height:30px" role="img" aria-label="Photo strip of pipelayer equipment on site"></div>

  <div class="brand">
    <span class="brand-dot"></span>
    <span class="brand-name">KolbyMarsh Inc.</span>
  </div>
  <div class="brand-rule" style="left:132px;top:145px;width:380px"></div>

  <div class="name">Reid Forbin</div>

  <ul class="contacts">
    <li><svg viewBox="0 0 16 16"><circle cx="8" cy="8" r="8" fill="#fff"/><path d="M5 4l2 2-1 1a5 5 0 003 3l1-1 2 2-1.5 1.5C7 12 4 9 3.5 5.5Z" fill="var(--green)"/></svg>555 418 9067</li>
    <li><svg viewBox="0 0 16 16"><rect x="1" y="3" width="14" height="10" fill="#fff"/><path d="M1 3l7 6 7-6" stroke="var(--green)" stroke-width="1.5" fill="none"/></svg>reid@kolbymarsh.ca</li>
    <li><svg viewBox="0 0 16 16"><circle cx="8" cy="8" r="7" stroke="#fff" stroke-width="1.5" fill="none"/><path d="M1 8h14M8 1c-3 4-3 10 0 14M8 1c3 4 3 10 0 14" stroke="#fff" stroke-width="1.2" fill="none"/></svg>kolbymarsh.ca</li>
    <li><svg viewBox="0 0 16 16"><path d="M8 1a5 5 0 015 5c0 4-5 9-5 9S3 10 3 6a5 5 0 015-5z" fill="#fff"/><circle cx="8" cy="6" r="2" fill="var(--green)"/></svg>RR4, Site2, Comp7 Pine Hollow, ZZ A0A 8K3</li>
  </ul>
</section>

</body>
</html>
```